Photobook template design

Just one book of 4/5 pages needed to find a handful of designers to help with this project that will be ongoing for several months, we will agree design price per book.

Hi there, we need lots of fabulous photobook templates designed:
there will be 20 books to start with, canvas layouts, calendar layouts etc.

The MAIN idea of the template is to facilitate the easiest creation / ordering of photobooks etc. possible for the client, so all they have to do is upload their pics and drop them into the templates you're going to design...

Each photobook needs to have min 20 pages, there can be a common theme throughout, but they must be different enough so that they do not all blend into one.
Choose to create a design from the following categories:
family
kids
travel
romance / love
seasonal holiday
year in review
everyday / general
recipes
pets / animals
collage
scrapbook

the quality and look and feel must be equal to www.pagerivo.example / www.snapduvel.example / www.framelyst.example.uk

In order to keep the designs as fresh as possible - we will work with several designers, so for this first project we will choose 1 designer, but then we'll create other design projects for which you will be specifically invited to design for - it's the only way the do multiple designs/projects.

please see 2 pics attached of other templates already designed - we're very happy with these...

Target Market(s)

These photobooks / calendars / canvas prints are for the average family - not too serious, must be fun / tongue in cheek etc.
They're for people who want to do photobooks but have no clue or do not have the time - so they must LOVE the design, and then want to just add their photos...

Industry/Entity Type

Travel

Requirements
Must have
• Must be designed in Indesign or Illustrator.
Metric sizes please - Either A3 landscape or portrait with 3 mm bleed, or 300 x 300mm square - 3mm bleed
If you place photos for proofing, please use imagorra images - we have a imagorra account

```html
<!DOCTYPE html>
<html lang="en">
<head>
<meta charset="utf-8">
<title>Moments With You – Romance Photobook</title>
<link href="https://fonts.googleapis.com/css2?family=Mulish:wght@300;400&display=swap" rel="stylesheet">
<style>
  :root{
    --backdrop:#e6e3de;
    --green:#3f8c34;
    --green-dark:#2f6f28;
    --orange:#c2701f;
    --orange-dark:#9a5414;
    --purple:#8e2a8e;
    --purple-dark:#6c1f70;
    --teal:#1c9ca8;
    --teal-dark:#137c88;
    --paper:#f2eee2;
    --ribbon:#cfc6b4;
    --frame-gold:#c9a57a;
    --lace:#9cc0a4;
    --label-orange:#bf6a2c;
    --label-magenta:#9e2a8f;
    --label-green:#3f8a3c;
    --label-teal:#1e9c9b;
    --body-text:#6a6458;
    --white:#ffffff;
  }
  *{box-sizing:border-box;margin:0;padding:0}
  html,body{width:1178px;height:1200px;overflow:hidden;background:var(--backdrop)}
  body{position:relative;font-family:"Mulish",sans-serif}

  .spread{position:absolute;left:44px;width:1090px;height:546px;box-shadow:0 4px 14px rgba(0,0,0,.18)}
  .spread--cover{top:40px}
  .spread--inner{top:614px;background:var(--paper)}
  .page{position:absolute;top:0;width:545px;height:546px;overflow:hidden}
  .page--left{left:0}
  .page--right{left:545px}
  .spine{position:absolute;left:544px;top:0;width:1px;height:100%;background:rgba(0,0,0,.12)}

  .band{position:absolute;left:0;width:100%}
  .band--top{top:0;height:272px}
  .band--bottom{top:272px;height:274px}
  .back .band--top{background:linear-gradient(180deg,#4a9a3a,var(--green) 60%,var(--green-dark))}
  .back .band--bottom{background:linear-gradient(180deg,var(--orange),#b3631b 60%,var(--orange-dark))}
  .front .band--top{background:linear-gradient(180deg,var(--purple),#9a2f94 40%,var(--purple-dark))}
  .front .band--bottom{background:linear-gradient(180deg,#1a8c9a,var(--teal) 60%,var(--teal-dark))}

  .continued-ribbon{position:absolute;left:0;top:254px;width:222px;height:40px}
  .continued-ribbon span{position:absolute;left:32px;top:9px;font-weight:300;font-size:17px;color:var(--white);letter-spacing:.3px}

  .cover-frame{position:absolute;left:51px;top:96px;width:452px;height:356px}
  .cover-title{position:absolute;left:0;width:100%;top:466px;text-align:center;font-weight:300;font-size:31px;color:var(--white);letter-spacing:.4px}

  .photo-slot{position:absolute;border:5px dotted var(--lace);padding:4px;background:var(--paper)}
  .photo-slot .photo{width:100%;height:100%}
  .photo--met{background:linear-gradient(135deg,#6b5a44,#8a7762 50%,#3c3530)}
  .photo--date{background:linear-gradient(160deg,#b5a77a,#d8cfae 45%,#6f7a3d)}
  .photo--kiss{background:linear-gradient(135deg,#8c8f5a,#cbb79c 50%,#6b6a45)}
  .photo--love{background:linear-gradient(160deg,#5a2a3a,#8d5a6a 50%,#3c2a2e)}

  .label{position:absolute;width:176px;height:30px;transform:translateX(-50%)}
  .label span{position:absolute;inset:0;display:flex;align-items:center;justify-content:center;font-size:11.5px;letter-spacing:1.2px;color:var(--white);font-weight:400}

  .story{position:absolute;width:214px;font-size:6.4px;line-height:1.32;color:var(--body-text);text-align:justify}
  .story p+p{margin-top:6px}

  .ornament{position:absolute;border-radius:50%}
  .ornament--flowers{background:radial-gradient(circle,rgba(240,160,90,.55),rgba(170,210,230,.35) 60%,transparent 72%)}
  .ornament--bloom{background:radial-gradient(circle,rgba(245,205,170,.45),transparent 70%)}
</style>
</head>
<body>

<section class="spread spread--cover">
  <div class="page page--left back">
    <div class="band band--top"></div>
    <div class="band band--bottom"></div>
    <div class="continued-ribbon">
      <svg width="222" height="40" viewBox="0 0 222 40"><polygon points="0,0 222,0 206,20 222,40 0,40" fill="var(--ribbon)"/></svg>
      <span>to be continued....</span>
    </div>
  </div>
  <div class="page page--right front">
    <div class="band band--top"></div>
    <div class="band band--bottom"></div>
    <svg class="cover-frame" viewBox="0 0 452 356" role="img" aria-label="Cover photo of a couple close together">
      <defs>
        <linearGradient id="coverPhoto" x1="0" y1="0" x2="1" y2="1">
          <stop offset="0" stop-color="#d9b49a"/>
          <stop offset=".5" stop-color="#e8c7a8"/>
          <stop offset="1" stop-color="#5a4a40"/>
        </linearGradient>
      </defs>
      <path d="M40 6 H190 Q226 30 262 6 H412 Q446 6 446 40 V150 Q432 178 446 206 V316 Q446 350 412 350 H262 Q226 326 190 350 H40 Q6 350 6 316 V206 Q20 178 6 150 V40 Q6 6 40 6 Z" fill="url(#coverPhoto)" stroke="var(--frame-gold)" stroke-width="7"/>
    </svg>
    <div class="cover-title">moments with you...</div>
  </div>
  <div class="spine"></div>
</section>

<section class="spread spread--inner">
  <div class="page page--left">
    <div class="ornament ornament--bloom" style="left:230px;top:240px;width:120px;height:120px" role="img" aria-label="Pale floral bloom decoration"></div>
    <div class="ornament ornament--flowers" style="left:22px;top:440px;width:130px;height:90px" role="img" aria-label="Cluster of drawn flowers"></div>

    <div class="photo-slot" style="left:32px;top:38px;width:232px;height:220px">
      <div class="photo photo--met" role="img" aria-label="Photo of the couple on the day they met"></div>
    </div>

    <div class="label" style="left:402px;top:77px">
      <svg width="176" height="30" viewBox="0 0 176 30"><polygon points="0,15 16,0 160,0 176,15 160,30 16,30" fill="var(--label-orange)"/><polygon points="10,15 20,4 156,4 166,15 156,26 20,26" fill="none" stroke="rgba(255,255,255,.5)" stroke-dasharray="2 2"/></svg>
      <span>HOW WE MET</span>
    </div>
    <div class="story" style="left:296px;top:118px">
      <p>Tell the story of this moment here. Add a few lines about where you were, what you did, and why it still makes you both smile today.</p>
      <p>Keep it short and sweet, or write a little more. Every page is yours to fill with the small details you never want to forget.</p>
    </div>

    <div class="label" style="left:148px;top:313px">
      <svg width="176" height="30" viewBox="0 0 176 30"><polygon points="0,15 16,0 160,0 176,15 160,30 16,30" fill="var(--label-green)"/><polygon points="10,15 20,4 156,4 166,15 156,26 20,26" fill="none" stroke="rgba(255,255,255,.5)" stroke-dasharray="2 2"/></svg>
      <span>OUR FIRST DATE</span>
    </div>
    <div class="story" style="left:40px;top:354px">
      <p>Tell the story of this moment here. Add a few lines about where you were, what you did, and why it still makes you both smile today.</p>
      <p>Keep it short and sweet, or write a little more. Every page is yours to fill with the small details you never want to forget.</p>
    </div>

    <div class="photo-slot" style="left:280px;top:284px;width:236px;height:216px">
      <div class="photo photo--date" role="img" aria-label="Photo of the couple on their first date outdoors"></div>
    </div>
  </div>

  <div class="page page--right">
    <div class="ornament ornament--bloom" style="left:195px;top:240px;width:120px;height:120px" role="img" aria-label="Pale floral bloom decoration"></div>
    <div class="ornament ornament--flowers" style="left:393px;top:440px;width:130px;height:90px" role="img" aria-label="Cluster of drawn flowers"></div>

    <div class="label" style="left:139px;top:77px">
      <svg width="176" height="30" viewBox="0 0 176 30"><polygon points="0,15 16,0 160,0 176,15 160,30 16,30" fill="var(--label-magenta)"/><polygon points="10,15 20,4 156,4 166,15 156,26 20,26" fill="none" stroke="rgba(255,255,255,.5)" stroke-dasharray="2 2"/></svg>
      <span>OUR FIRST KISS</span>
    </div>
    <div class="story" style="left:37px;top:118px">
      <p>Tell the story of this moment here. Add a few lines about where you were, what you did, and why it still makes you both smile today.</p>
      <p>Keep it short and sweet, or write a little more. Every page is yours to fill with the small details you never want to forget.</p>
    </div>

    <div class="photo-slot" style="left:281px;top:38px;width:238px;height:220px">
      <div class="photo photo--kiss" role="img" aria-label="Photo of the couple's first kiss"></div>
    </div>

    <div class="photo-slot" style="left:29px;top:284px;width:234px;height:216px">
      <div class="photo photo--love" role="img" aria-label="Photo of the couple embracing among flowers"></div>
    </div>

    <div class="label" style="left:397px;top:313px">
      <svg width="176" height="30" viewBox="0 0 176 30"><polygon points="0,15 16,0 160,0 176,15 160,30 16,30" fill="var(--label-teal)"/><polygon points="10,15 20,4 156,4 166,15 156,26 20,26" fill="none" stroke="rgba(255,255,255,.5)" stroke-dasharray="2 2"/></svg>
      <span>FIRST I LOVE YOU</span>
    </div>
    <div class="story" style="left:289px;top:354px">
      <p>Tell the story of this moment here. Add a few lines about where you were, what you did, and why it still makes you both smile today.</p>
      <p>Keep it short and sweet, or write a little more. Every page is yours to fill with the small details you never want to forget.</p>
    </div>
  </div>
  <div class="spine"></div>
</section>

</body>
</html>
```